ROB & JO’S GOODBYE TO MIDGE BITES

I require an attractive appealing label with the dimensions 7.5m x 3.5cm
This is a Natural sandfly insect repellent cream formulated by 2 pharmacists Carla Whitby and Rob Kettering. It is required for labelling a 50 g jar

Contains Essential Oils of cedar wood, rosemary, cinnamon, citronella, lavender, eucalyptus and clove in a moisturising base.

We would like to see designs using the colour bright duck egg blue as the main colour with dark brown tones for the patterns. An eye catching label is output aim . However any colour combination that is attractive to the eye is welcome
A gloss finish is preferable.

More designs please

Target Market(s)

Trekkers, outdoor active people, pharmacy, health shops

Colors
abd037
34a6d7
0456a4
33b8a4

Requirements
Must have
• Rob and Jo’s
• Goodbye to Midge bites
• Natural Sandfly Repellent
• Contains Essential Oils of cedar wood, rosemary, cinnamon, citronella, lavender, eucalyptus and clove in a moisturising base.
• Formulated by Australian Pharmacists Carla Whitby and Rob Kettering
• Made in Australia
• 0413862207
Nice to have
• Sandfly/ flies
• I have attached a label I use for my mozzie cream and would like a similar font please

```html
<!DOCTYPE html>
<html lang="en">
<head>
<meta charset="utf-8">
<title>Rob &amp; Jo’s Natural Repellent Label</title>
<link href="https://fonts.googleapis.com/css2?family=Yellowtail&family=Lobster+Two:ital,wght@1,700&family=Playfair+Display:ital,wght@0,500;1,600&display=swap" rel="stylesheet">
<style>
  :root {
    --night: #000000;
    --bark: #3b3322;
    --lime: #66f20f;
    --mint: #4ff0a4;
    --cream: #f4fde9;
    --ink: #141414;
    --white: #ffffff;
    --wing: #b8c43a;
  }
  html, body { margin: 0; padding: 0; overflow: hidden; background: var(--night); }
  .label {
    position: relative;
    width: 1200px;
    height: 559px;
    overflow: hidden;
    background: linear-gradient(100deg, var(--night) 0%, var(--night) 45%, #17140d 65%, var(--bark) 100%);
  }
  .label__band { position: absolute; inset: 0; }
  .brand-leaf { position: absolute; left: -30px; top: -40px; width: 420px; height: 330px; }
  .brand-owner {
    position: absolute; left: 100px; top: 42px; width: 210px; text-align: center;
    font-family: "Playfair Display", serif; font-style: italic; font-weight: 600;
    font-size: 24px; color: var(--white); letter-spacing: 1px;
  }
  .brand-mark {
    position: absolute; left: 80px; top: 78px; width: 250px; text-align: center;
    font-family: "Yellowtail", cursive; font-size: 84px; line-height: 1; color: var(--ink);
  }
  .product-title {
    position: absolute; left: 440px; top: 30px; width: 400px; text-align: center;
    font-family: "Yellowtail", cursive; color: var(--mint);
    transform: rotate(-9deg); line-height: 1.05;
  }
  .product-title span { display: block; font-size: 54px; }
  .insect-art {
    position: absolute; left: 866px; top: 27px; width: 217px; height: 170px;
    border-radius: 50%;
    background: radial-gradient(ellipse at center, rgba(184,196,58,0.35) 0%, rgba(184,196,58,0.12) 55%, rgba(184,196,58,0) 75%);
  }
  .product-name {
    position: absolute; left: 800px; top: 230px; width: 390px; text-align: center;
    font-family: "Playfair Display", serif; font-weight: 500; font-size: 27px;
    letter-spacing: 1px; color: var(--white);
  }
  .details {
    position: absolute; left: 0; top: 374px; width: 1200px; text-align: center;
    font-family: "Lobster Two", cursive; font-style: italic; font-weight: 700;
    font-size: 20px; line-height: 25px; color: var(--ink);
  }
  .details p { margin: 0; }
  .details .gap { margin-top: 22px; }
</style>
</head>
<body>
<main class="label">
  <svg class="label__band" viewBox="0 0 1200 559" aria-hidden="true">
    <defs>
      <radialGradient id="creamGlow" cx="0.5" cy="0.15" r="0.9">
        <stop offset="0" stop-color="#ffffff"/>
        <stop offset="1" stop-color="#eef9dd"/>
      </radialGradient>
    </defs>
    <path d="M0 405 C 120 340, 300 312, 520 306 C 760 300, 980 302, 1200 306 L1200 559 L0 559 Z" fill="url(#creamGlow)"/>
  </svg>

  <svg class="brand-leaf" viewBox="0 0 420 330" role="img" aria-label="Bright lime leaf shape behind the brand name">
    <ellipse cx="215" cy="170" rx="205" ry="125" transform="rotate(-18 215 170)" fill="#66f20f"/>
  </svg>
  <div class="brand-owner">ROB &amp; JO’S</div>
  <div class="brand-mark">RJG</div>

  <h1 class="product-title"><span>Natural</span><span>Mozzie Repellent</span></h1>

  <div class="insect-art" role="img" aria-label="Line illustration of a winged sandfly"></div>
  <div class="product-name">GOODBYE TO MOZZIES</div>

  <section class="details">
    <p>Goodbye to Midge bites- Natural Sandfly Repellent</p>
    <p>- Contains Essential Oils of cedar wood, rosemary, cinnamon,</p>
    <p>citronella, lavender, eucalyptus and clove in a moisturising base.</p>
    <p class="gap">- Formulated by Australian Pharmacists Carla Whitby and Rob Kettering</p>
    <p>- Made in Australia - 0413862207</p>
  </section>
</main>
</body>
</html>
```